Business card for communications

Need a business card for my consulting business - I work with not for profits, start ups and social enterprises on their media, communications campaigns.

Please see my website for colours, images and fonts www.morvenquillet.example

Morven Quillet
Communications & Campaign strategist
Sydney - Melbourne
M: 0498 317 250
E: morven@morvenquillet.example
S: morvenquillet
W: morvenquillet.example
T: @morvenquillet

(above is info only and can be presented any way e.g. should not have to be M for mobile - it should be an icon)
Updates

Dear designers I have updated the brief and uploaded high res images from my website for you to use. The designs so far with the use of images and icons are much better so far. Thank you I look forward to receiving your revised designs. Morven Quillet

Industry/Entity Type

Communications

Font styles to use
Sans Serif

Requirements
Must have
• Icons for contact details
Images from the website www.morvenquillet.example
Nice to have
• Images - attached

```html
<!DOCTYPE html>
<html lang="en">
<head>
<meta charset="utf-8">
<title>Morven Quillet – Business Card</title>
<link rel="stylesheet" href="https://fonts.googleapis.com/css2?family=Josefin+Sans:wght@700&family=Lato:wght@400;700&display=swap">
<style>
  :root {
    --canvas: #f2f2f2;
    --card: #ffffff;
    --yellow: #f9d230;
    --ink: #6b6b6b;
    --ink-dark: #555555;
    --icon: #5a5a5a;
    --wood-light: #b07a45;
    --wood-dark: #6e4524;
  }
  * { box-sizing: border-box; margin: 0; padding: 0; }
  html, body { width: 1200px; height: 900px; overflow: hidden; }
  body {
    position: relative;
    background: var(--canvas);
    font-family: "Lato", "Helvetica Neue", Arial, sans-serif;
    color: var(--ink);
  }
  .card { position: absolute; background: var(--card); overflow: hidden; }

  /* Front */
  .card--front { left: 87px; top: 42px; width: 796px; height: 418px; z-index: 2; }
  .front__photo {
    position: absolute; left: 0; top: 0; width: 796px; height: 334px;
    background:
      radial-gradient(ellipse at 30% 40%, rgba(255,255,255,.18), transparent 55%),
      radial-gradient(ellipse at 75% 70%, rgba(255,255,255,.14), transparent 50%),
      linear-gradient(135deg, var(--wood-light), var(--wood-dark));
  }
  .front__band {
    position: absolute; left: 0; top: 334px; width: 796px; height: 84px;
    background: var(--yellow);
    display: flex; align-items: center; padding-left: 53px;
  }
  .front__name {
    font-family: "Josefin Sans", "Futura", sans-serif;
    font-weight: 700; font-size: 29px; letter-spacing: 1.5px;
    color: var(--ink); padding-top: 6px;
  }
  .front__divider { width: 2px; height: 30px; background: var(--ink); margin: 0 11px 0 14px; }
  .front__title { font-size: 16px; color: var(--ink-dark); }

  /* Back */
  .card--back { left: 313px; top: 432px; width: 798px; height: 420px; border: 1px solid #d8d8d8; z-index: 1; }
  .contact-list { position: absolute; left: 70px; top: 67px; list-style: none; }
  .contact-list li { display: flex; align-items: center; height: 46px; font-size: 19px; color: var(--ink-dark); }
  .contact-icon {
    width: 40px; height: 40px; border-radius: 50%; background: var(--yellow);
    display: flex; align-items: center; justify-content: center; margin-right: 10px;
    color: var(--icon); font-weight: 700; font-size: 24px;
  }
  .identity { position: absolute; left: 454px; top: 52px; }
  .identity__name {
    font-family: "Josefin Sans", "Futura", sans-serif;
    font-weight: 700; font-size: 30px; letter-spacing: 1.5px; color: var(--ink);
    margin-bottom: 8px;
  }
  .identity__line { font-size: 16px; color: var(--ink-dark); line-height: 21px; }
  .services {
    position: absolute; left: 0; bottom: 0; width: 798px; height: 92px;
    background: var(--yellow); display: flex; align-items: center;
  }
  .service { font-size: 16px; line-height: 21px; text-transform: uppercase; color: var(--ink); }
  .service-divider { width: 3px; height: 44px; background: var(--ink); }
</style>
</head>
<body>

<section class="card card--front">
  <div class="front__photo" role="img" aria-label="Overhead photo of a shared wooden desk with laptops, keyboards, folders and coffee cups"></div>
  <div class="front__band">
    <span class="front__name">MORVEN QUILLET</span>
    <span class="front__divider"></span>
    <span class="front__title">Communications &amp; Campaign strategist</span>
  </div>
</section>

<section class="card card--back">
  <ul class="contact-list">
    <li>
      <span class="contact-icon">
        <svg width="24" height="24" viewBox="0 0 24 24" aria-hidden="true">
          <path d="M3 9c0-3 4-5 9-5s9 2 9 5v2h-5V8.5c-2-.7-6-.7-8 0V11H3z" fill="var(--icon)"/>
          <path d="M6 12h12l2 8H4z" fill="var(--icon)"/>
          <circle cx="12" cy="16" r="2.5" fill="var(--yellow)"/>
        </svg>
      </span>0498 317 250
    </li>
    <li>
      <span class="contact-icon">
        <svg width="24" height="20" viewBox="0 0 24 20" aria-hidden="true">
          <rect x="1" y="3" width="22" height="14" fill="var(--icon)"/>
          <path d="M1 3l11 8 11-8" fill="none" stroke="var(--yellow)" stroke-width="1.5"/>
        </svg>
      </span>morven@morvenquillet.example
    </li>
    <li><span class="contact-icon"></span>morvenquillet</li>
    <li><span class="contact-icon">@</span>morvenquillet.example</li>
    <li><span class="contact-icon"></span>morvenquillet.example</li>
  </ul>

  <div class="identity">
    <div class="identity__name">MORVEN QUILLET</div>
    <div class="identity__line">Communications &amp; Campaign strategist</div>
    <div class="identity__line">Sydney - Melbourne</div>
  </div>

  <div class="services">
    <span class="service" style="margin-left:63px;width:184px">Communications<br>Strategy</span>
    <span class="service-divider"></span>
    <span class="service" style="margin-left:34px;width:123px">Media<br>Relations</span>
    <span class="service-divider"></span>
    <span class="service" style="margin-left:35px;width:152px">PR &amp;<br>Campaigns</span>
    <span class="service-divider"></span>
    <span class="service" style="margin-left:35px">Strategic<br>Counsel</span>
  </div>
</section>

</body>
</html>
```